Professional Sales Business looking for inspirational poster

I need an inspirational poster design for sales professionals, targeted around the phrase "Win Fast, Lose Fast". The style of the poster will be primarily minimalistic and flat with the main focus being on the phrase, however, any graphics or creative font and background styles are encouraged. Color choice is up to you.

Design Specs:
Vector files are best. If creating a vector file isn't possible, 150dpi raster images (at actual size or bigger) are good too. The poster must be in a portrait layout and scalable to the sizes of 18" X 24" and 24" X 36". Please convert all text to outlines.

Please msg me if you have any additional questions.

```html
<!DOCTYPE html>
<html lang="en">
<head>
<meta charset="utf-8">
<title>Win Fast Lose Fast — Sales Poster</title>
<link rel="stylesheet" href="https://fonts.googleapis.com/css2?family=Oswald:wght@700&display=swap">
<style>
  :root {
    --red-deep: #8e0a0c;
    --red-mid: #c8161a;
    --red-bright: #e2281c;
    --floor-top: #a8090c;
    --floor-bottom: #5c0406;
    --glow-orange: #ff7a1f;
    --type-light: #ffffff;
    --type-shade: #c9c9c9;
  }
  html, body {
    margin: 0;
    padding: 0;
    width: 802px;
    height: 1200px;
    overflow: hidden;
    background: var(--red-deep);
  }
  .poster {
    position: relative;
    width: 802px;
    height: 1200px;
    overflow: hidden;
  }
  .poster-art {
    position: absolute;
    inset: 0;
    display: block;
  }
  .headline {
    font-family: "Oswald", "Arial Narrow", sans-serif;
    font-weight: 700;
    font-size: 172px;
    letter-spacing: -3px;
  }
</style>
</head>
<body>
<main class="poster">
  <svg class="poster-art" width="802" height="1200" viewBox="0 0 802 1200" xmlns="http://www.w3.org/2000/svg">
    <defs>
      <radialGradient id="wallGlow" cx="55%" cy="35%" r="70%">
        <stop offset="0" stop-color="var(--red-bright)"/>
        <stop offset="0.55" stop-color="var(--red-mid)"/>
        <stop offset="1" stop-color="var(--red-deep)"/>
      </radialGradient>
      <linearGradient id="floorShade" x1="0" y1="0" x2="0" y2="1">
        <stop offset="0" stop-color="var(--floor-top)"/>
        <stop offset="1" stop-color="var(--floor-bottom)"/>
      </linearGradient>
      <linearGradient id="letterFace" x1="0" y1="0" x2="0" y2="1">
        <stop offset="0" stop-color="var(--type-shade)"/>
        <stop offset="0.5" stop-color="var(--type-light)"/>
        <stop offset="1" stop-color="var(--type-light)"/>
      </linearGradient>
      <linearGradient id="reflectionFade" x1="0" y1="0" x2="0" y2="1">
        <stop offset="0" stop-color="#ffffff" stop-opacity="0.45"/>
        <stop offset="0.6" stop-color="#ffffff" stop-opacity="0"/>
      </linearGradient>
      <filter id="letterShadow" x="-10%" y="-10%" width="120%" height="130%">
        <feDropShadow dx="0" dy="4" stdDeviation="5" flood-color="#4a0000" flood-opacity="0.5"/>
      </filter>
    </defs>

    <!-- backdrop wall -->
    <rect class="backdrop-wall" x="0" y="0" width="802" height="834" fill="url(#wallGlow)"/>

    <!-- translucent accent squares -->
    <g class="accent-squares">
      <rect x="300" y="-220" width="420" height="420" fill="var(--glow-orange)" opacity="0.28" transform="rotate(-28 510 -10)"/>
      <rect x="330" y="-60" width="380" height="380" fill="var(--glow-orange)" opacity="0.22" transform="rotate(-32 520 130)"/>
      <rect x="80" y="-150" width="360" height="360" fill="var(--glow-orange)" opacity="0.14" transform="rotate(-22 260 30)"/>
    </g>

    <!-- floor -->
    <rect class="floor" x="0" y="834" width="802" height="366" fill="url(#floorShade)"/>
    <line class="horizon" x1="0" y1="834" x2="802" y2="834" stroke="#7a0508" stroke-width="2"/>

    <!-- headline -->
    <g class="headline" text-anchor="middle" fill="url(#letterFace)" filter="url(#letterShadow)">
      <text x="401" y="353">WIN</text>
      <text x="401" y="505">FAST</text>
      <text x="401" y="657">LOSE</text>
      <text x="401" y="809">FAST</text>
    </g>

    <!-- floor reflection -->
    <g class="headline reflection" text-anchor="middle" fill="url(#reflectionFade)" transform="translate(0 1668) scale(1 -1)" opacity="0.7">
      <text x="401" y="809">FAST</text>
    </g>
  </svg>
</main>
</body>
</html>
```